Raised Fingerprint Business Card Design

I need a business card design and I would like the image for the business cards to carry on to my stationary and website. My business is Forensic Consulting. I will be providing services to prosecuting and defense attorneys as well as law enforcement agencies in the areas of latent print comparison, crime scene investigations, and forensic training. I am looking for a color scheme of red, black, and silver. I would like a fingerprint that is raised and the text to be raised to some degree depending on your recommendations. with a fingerprint glass. I would like the card to include the business name, my name the deignation CLPE after it, phone number, web address, and physical address. I would like the phrase "veritas aequitas " placed discretely at the bottome of the card-subtle/not too bold.

Target Market(s)

Attorneys and law enforcement agencies

Industry/Entity Type

Business

Contact Information for Business Card

Dora Pilcott, CLPE
Pilcott Trace Advisors, LLC
P.O. Box 731592 Sacramento, CA 95817
916.555.0148
www.pilcotttraceadvisors.com
pilcotttrace@mailvane.com

Colors
ec1f27

Requirements
Must have
• Fingerprint and old fashioned handheld magnifying glass (Barnaby Quist style.
• The Latin phrase listed above placed at the bottom of the front of the card discreetly.
Nice to have
• The fingerprint ridges (black lines) raised so the customer can feel it the texture.
• Raised lettering for either my name or the company name.
Should not have
• None that I can think of now.

```html
<!DOCTYPE html>
<html lang="en">
<head>
<meta charset="utf-8">
<title>Pilcott Trace Advisors — Business Card</title>
<link rel="stylesheet" href="https://fonts.googleapis.com/css2?family=Sorts+Mill+Goudy&family=Questrial&display=swap">
<style>
  :root {
    --page-bg: #d9d6d2;
    --card-black: #0d0d0e;
    --card-charcoal: #2a2b2d;
    --card-silver: #5a5c60;
    --blood-red: #ec1f27;
    --blood-dark: #7d0a0e;
    --text-white: #f2f2f2;
    --text-silver: #b9bbbe;
    --ribbon-white: #ffffff;
    --name-navy: #1b2340;
    --title-maroon: #8b1a1a;
    --frame-line: #3a3b3e;
  }
  * { box-sizing: border-box; margin: 0; padding: 0; }
  html, body { width: 1200px; height: 750px; overflow: hidden; }
  body {
    background: var(--page-bg);
    font-family: "Sorts Mill Goudy", Georgia, serif;
    position: relative;
  }
  .card {
    position: absolute;
    top: 220px;
    width: 540px;
    height: 310px;
    overflow: hidden;
    box-shadow: 0 8px 22px rgba(0,0,0,.35);
  }

  /* Front */
  .card-front {
    left: 40px;
    background: radial-gradient(ellipse at 38% 58%, var(--card-silver) 0%, var(--card-charcoal) 40%, var(--card-black) 100%);
  }
  .front-blood {
    position: absolute; left: 0; top: 0; width: 160px; height: 140px;
    background: radial-gradient(ellipse at 40% 20%, rgba(200,20,28,.9) 0%, rgba(125,10,14,.55) 45%, rgba(125,10,14,0) 75%);
  }
  .front-print-glass {
    position: absolute; left: 300px; top: 40px; width: 220px; height: 262px;
    background: radial-gradient(circle at 45% 42%, #6e7074 0%, #2a2a2c 45%, #111 75%, rgba(17,17,17,0) 100%);
  }
  .front-name {
    position: absolute; left: 40px; top: 158px;
    color: var(--text-white);
    font-size: 28px;
    letter-spacing: .5px;
    text-shadow: 0 2px 3px rgba(0,0,0,.8);
  }
  .front-web {
    position: absolute; left: 40px; top: 222px;
    color: var(--blood-red);
    font-size: 11px;
    letter-spacing: 3.6px;
  }
  .front-motto {
    position: absolute; left: 40px; top: 250px;
    color: var(--text-silver);
    font-size: 9px;
    letter-spacing: 2px;
  }

  /* Back */
  .card-back {
    left: 620px;
    background: radial-gradient(ellipse at 30% 65%, #2b2c2f 0%, #131315 55%, var(--card-black) 100%);
  }
  .back-frame {
    position: absolute; inset: 10px;
    border: 1px solid var(--frame-line);
  }
  .back-drip {
    position: absolute; left: 30px; top: 0; width: 90px; height: 240px;
    background: linear-gradient(180deg, rgba(160,16,22,.85) 0%, rgba(220,40,36,.9) 70%, rgba(220,40,36,0) 100%);
    border-radius: 0 0 45px 45px;
  }
  .back-splatter {
    position: absolute; right: 10px; top: 0; width: 160px; height: 90px;
    background: radial-gradient(ellipse at 60% 50%, rgba(200,20,28,.9) 0%, rgba(125,10,14,.5) 50%, rgba(125,10,14,0) 78%);
  }
  .back-ribbon {
    position: absolute; left: 210px; right: 0; top: 90px; height: 54px;
    background: var(--ribbon-white);
    box-shadow: 0 3px 6px rgba(0,0,0,.5);
  }
  .back-ribbon::before {
    content: ""; position: absolute; left: -27px; top: 0;
    width: 54px; height: 54px; border-radius: 50%;
    background: #141416;
  }
  .back-name {
    position: absolute; right: 42px; top: 2px;
    color: var(--name-navy);
    font-size: 27px;
    letter-spacing: 1px;
  }
  .back-title {
    position: absolute; right: 42px; top: 32px;
    color: var(--title-maroon);
    font-family: Georgia, serif;
    font-weight: bold;
    font-size: 15px;
  }
  .back-company {
    position: absolute; right: 42px; top: 162px;
    color: var(--blood-red);
    font-size: 18px;
    letter-spacing: .5px;
  }
  .contact-list {
    position: absolute; right: 32px; top: 204px;
    list-style: none;
    font-family: "Questrial", Arial, sans-serif;
    font-size: 10px;
    color: var(--text-white);
  }
  .contact-item {
    display: flex; align-items: center; justify-content: flex-end;
    gap: 8px; height: 24px;
  }
  .contact-icon { width: 18px; height: 18px; }
</style>
</head>
<body>

<section class="card card-front" aria-label="Card front">
  <div class="front-blood" role="img" aria-label="Blood drips running down from the top edge"></div>
  <div class="front-print-glass" role="img" aria-label="Raised fingerprint under an old-fashioned handheld magnifying glass"></div>
  <h1 class="front-name">Pilcott Trace Advisors</h1>
  <p class="front-web">www.pilcotttraceadvisors.com</p>
  <p class="front-motto">veritas aequitas</p>
</section>

<section class="card card-back" aria-label="Card back">
  <div class="back-drip" role="img" aria-label="Long blood drip from the top edge"></div>
  <div class="back-splatter" role="img" aria-label="Blood splatter in the top corner"></div>
  <div class="back-frame"></div>
  <div class="back-ribbon">
    <h2 class="back-name">Dora Pilcott</h2>
    <p class="back-title">CLPE</p>
  </div>
  <p class="back-company">Pilcott Trace Advisors</p>
  <ul class="contact-list">
    <li class="contact-item">
      <span>P.O. Box 731592 Sacramento, CA 95817</span>
      <svg class="contact-icon" viewBox="0 0 18 18" aria-hidden="true">
        <circle cx="9" cy="9" r="9" fill="#e0413a"/>
        <path d="M9 4a3 3 0 0 1 3 3c0 2.3-3 6-3 6s-3-3.7-3-6a3 3 0 0 1 3-3z" fill="#fff"/>
        <circle cx="9" cy="7" r="1.1" fill="#e0413a"/>
      </svg>
    </li>
    <li class="contact-item">
      <span>916.555.0148</span>
      <svg class="contact-icon" viewBox="0 0 18 18" aria-hidden="true">
        <circle cx="9" cy="9" r="9" fill="#e0413a"/>
        <path d="M6.2 4.6l1.5 1.6-.8 1.4c.6 1.3 1.5 2.2 2.8 2.8l1.4-.8 1.6 1.5-.9 1.6C9 12.5 5.5 9 5.3 5.5z" fill="#fff"/>
      </svg>
    </li>
    <li class="contact-item">
      <span>pilcotttrace@mailvane.com</span>
      <svg class="contact-icon" viewBox="0 0 18 18" aria-hidden="true">
        <circle cx="9" cy="9" r="9" fill="#e0413a"/>
        <rect x="4.5" y="6" width="9" height="6.5" fill="#fff"/>
        <path d="M4.5 6l4.5 3.6L13.5 6" fill="none" stroke="#e0413a" stroke-width="1"/>
      </svg>
    </li>
  </ul>
</section>

</body>
</html>
```